Urine collection cup with and without sterile seal sticker

Hello. We need a urine cup label designed please with

Name:
Date of Birth:
Date:
Time:
Temp℃:
Specimen ID:

Product code: KTX-58
Volume markings (e.g., 30 mL, 60 mL, 90 mL).
Vesk Lab Checks logo

Could you please provide one version with the additional sterile sticker extending to the top, and one version without the additional sterile sticker?

```html
<!DOCTYPE html>
<html lang="en">
<head>
<meta charset="utf-8">
<title>Vesk Lab Checks – Collection Cup Labels</title>
<link href="https://fonts.googleapis.com/css2?family=Roboto+Condensed:wght@700&family=Montserrat:wght@500;600;700&display=swap" rel="stylesheet">
<style>
  :root {
    --backdrop: #cdbca4;
    --paper: #ffffff;
    --brand-blue: #29a1e2;
    --brand-blue-soft: #8fd0f2;
    --ink: #111111;
    --rule: #8c8c8c;
  }
  * { margin: 0; padding: 0; box-sizing: border-box; }
  html, body { width: 1153px; height: 1200px; overflow: hidden; background: var(--backdrop); }
  .canvas { position: relative; width: 1153px; height: 1200px; }

  .label {
    position: absolute;
    width: 805px; height: 474px;
    background: var(--paper);
    border-radius: 48px;
    overflow: hidden;
  }
  .label--standard { left: 46px; top: 105px; border-top-right-radius: 0; }
  .label--sterile  { left: 272px; top: 623px; border-top-right-radius: 0; }

  .fields { position: absolute; left: 41px; top: 0; width: 572px; }
  .field {
    position: absolute; left: 0; width: 572px;
    border-bottom: 2px solid var(--rule);
    font-family: "Roboto Condensed", sans-serif;
    font-weight: 700; font-size: 26px; color: var(--ink);
    line-height: 1; padding-bottom: 9px;
  }
  .field:nth-child(1) { top: 40px; }
  .field:nth-child(2) { top: 99px; }
  .field:nth-child(3) { top: 159px; }
  .field:nth-child(4) { top: 217px; }
  .field:nth-child(5) { top: 277px; }
  .field:nth-child(6) { top: 336px; }

  .brand {
    position: absolute; left: 0; width: 638px; top: 408px;
    display: flex; justify-content: center; align-items: center; gap: 8px;
    font-family: "Montserrat", sans-serif; font-weight: 700;
    font-size: 27px; color: var(--brand-blue);
  }
  .brand-dot { width: 30px; height: 30px; border-radius: 50%; background: var(--brand-blue); }

  .panel {
    position: absolute; right: 0; top: 0;
    width: 167px; height: 100%;
    background: var(--brand-blue);
    color: var(--paper);
    font-family: "Montserrat", sans-serif;
    text-align: center;
  }
  .emblem {
    position: absolute; left: 16px; top: 22px;
    width: 134px; height: 134px; border-radius: 50%;
    border: 3px solid var(--paper);
    background: linear-gradient(150deg, var(--brand-blue-soft), var(--brand-blue));
  }
  .divider { position: absolute; left: 7px; right: 7px; border-top: 3px dotted var(--paper); }
  .divider.upper { top: 233px; }
  .divider.lower { top: 336px; }
  .code-label { position: absolute; left: 0; right: 0; top: 260px; font-size: 14px; font-weight: 600; line-height: 1; }
  .code { position: absolute; left: 0; right: 0; top: 276px; font-size: 31px; font-weight: 600; line-height: 1; }
  .volume { position: absolute; left: 0; right: 0; top: 372px; font-size: 60px; font-weight: 700; line-height: 1; }
  .volume sup { font-size: 22px; font-weight: 600; vertical-align: 26px; margin-left: 2px; }

  .label--sterile .code { font-size: 27px; top: 279px; }

  .seal-tab {
    position: absolute; left: 910px; top: 418px;
    width: 167px; height: 260px;
    background: var(--brand-blue);
  }
  .seal-disc {
    position: absolute; left: 872px; top: 297px;
    width: 242px; height: 242px; border-radius: 50%;
    background: var(--brand-blue);
  }
  .seal-disc .emblem { left: 22px; top: 22px; width: 198px; height: 198px; }

  .seal-word, .seal-note {
    position: absolute; top: 550px; height: 276px;
    writing-mode: vertical-rl; transform: rotate(180deg);
    font-family: "Montserrat", sans-serif; color: var(--paper);
    white-space: nowrap; line-height: 1;
  }
  .seal-word { left: 953px; font-size: 62px; font-weight: 700; letter-spacing: 1px; }
  .seal-note { left: 1016px; font-size: 13.5px; font-weight: 600; }
</style>
</head>
<body>
<main class="canvas">

  <section class="label label--standard" aria-label="Collection cup label">
    <div class="fields">
      <div class="field">NAME</div>
      <div class="field">DOB</div>
      <div class="field">DATE</div>
      <div class="field">TIME</div>
      <div class="field">TEMP</div>
      <div class="field">SPECIMEN ID</div>
    </div>
    <div class="brand"><span class="brand-dot"></span>Vesk Lab Checks</div>
    <div class="panel">
      <div class="emblem" role="img" aria-label="Brand emblem area"></div>
      <div class="divider upper"></div>
      <div class="code-label">PRODUCT CODE:</div>
      <div class="code">KTX-58</div>
      <div class="divider lower"></div>
      <div class="volume">90<sup>ML</sup></div>
    </div>
  </section>

  <div class="seal-tab"></div>
  <div class="seal-disc">
    <div class="emblem" role="img" aria-label="Brand emblem area"></div>
  </div>

  <section class="label label--sterile" aria-label="Sterile collection cup label">
    <div class="fields">
      <div class="field">NAME</div>
      <div class="field">DOB</div>
      <div class="field">DATE</div>
      <div class="field">TIME</div>
      <div class="field">TEMP</div>
      <div class="field">SPECIMEN ID</div>
    </div>
    <div class="brand"><span class="brand-dot"></span>Vesk Lab Checks</div>
    <div class="panel">
      <div class="divider upper"></div>
      <div class="code-label">PRODUCT CODE:</div>
      <div class="code">KTX-58-S</div>
      <div class="divider lower"></div>
      <div class="volume">90<sup>ML</sup></div>
    </div>
  </section>

  <div class="seal-word">STERILE</div>
  <div class="seal-note">INTERIOR IF SEAL IS NOT BROKEN</div>

</main>
</body>
</html>
```